Business software developers new website

We need to redesign our website. Our current website is http://www.plumvista.net/index.html, which is outdated and needs a new look. We moved out from web design and have concentrated more on the back end of the systems, for example, system support and security and cloud-based applications. Our major clients include both private and government sectors. We would like to see some designs that are all in one page, simple and clean. Prefer illustrator or obstructed images instead of real-life photos. Must look futuristic yet friendly. Attached the new logo for your references and good luck.

Target Market(s)

Medium to big company for their IT or data management. Either improve or upgrade their current system.

Industry/Entity Type

Business Software

Number of Pages Required

1 page

Colors

Designer to choose colors to be used in the design.

Requirements
Must have
• Simple and clean. Individual assets must be provided in the correct size and format(png or jpeg). Prefer Goggle fonts. Even though the logo color is red, grey and black, still prefer some modern colors that go well with red. When design, must consider the possibility to convert it into responsive.
Nice to have
• White background
Should not have
• real life photos, no slider

```html
<!DOCTYPE html>
<html lang="en">
<head>
<meta charset="utf-8">
<title>plumvista.net — Simplifying the way you work</title>
<link href="https://fonts.googleapis.com/css2?family=Dosis:wght@500;600;700&family=Roboto:wght@400;500;700&display=swap" rel="stylesheet">
<style>
:root{
  --red:#f20f0c;
  --ink:#1e1e1e;
  --text:#555;
  --muted:#8a8a8a;
  --sky:#aeecee;
  --teal:#8ad5de;
  --cream:#fdfbea;
  --dark:#2b2b2b;
  --row-a:#f6f6f6;
  --row-b:#fbfbfb;
  --white:#fff;
}
*{box-sizing:border-box;margin:0;padding:0}
html,body{width:1200px;height:2744px;overflow:hidden}
body{position:relative;background:var(--white);font-family:"Roboto",Arial,sans-serif;color:var(--text)}
.abs{position:absolute}
.heading{font-family:"Dosis","Trebuchet MS",sans-serif}

/* header */
.site-header{left:0;top:0;width:1200px;height:68px;background:var(--white)}
.brand{left:161px;top:14px}
.brand-name{font-family:"Dosis",sans-serif;font-weight:700;font-size:27px;line-height:26px;color:var(--ink);letter-spacing:-.5px}
.brand-tag{font-size:9px;color:#777;font-weight:500;margin-top:1px}
.main-nav{left:431px;top:27px;width:428px;display:flex;justify-content:space-between;font-size:10px;font-weight:500;color:var(--ink);text-transform:uppercase;white-space:nowrap}
.main-nav .active{color:var(--red)}
.btn-signup,.btn-login{top:22px;height:22px;font-size:10px;font-weight:700;color:var(--white);display:flex;align-items:center;justify-content:center;gap:5px;border-radius:2px}
.btn-signup{left:881px;width:76px;background:var(--red)}
.btn-login{left:964px;width:76px;background:var(--teal)}

/* hero */
.hero{left:0;top:68px;width:1200px;height:462px;background:var(--sky)}
.hero-fade{left:0;top:500px;width:1200px;height:60px;background:linear-gradient(var(--sky),var(--white))}
.hero-title{left:0;width:1200px;top:110px;text-align:center;font-size:25px;font-weight:700;color:var(--ink)}
.hero-sub{left:0;width:1200px;top:150px;text-align:center;font-size:11.5px;color:#333}
.hero-btn{left:553px;top:185px;width:94px;height:27px;background:var(--white);color:var(--red);font-size:10px;font-weight:700;display:flex;align-items:center;justify-content:center;gap:4px}
.hero-art{left:450px;top:228px;width:300px;height:280px;border-radius:24px;background:linear-gradient(160deg,#9fdde3 0%,#8fd2da 45%,#f5a3a2 70%,#9fdde3 100%)}

/* about */
.about-label{left:161px;top:666px;font-size:12px;color:var(--red);display:flex;align-items:center;gap:8px;text-transform:uppercase}
.rule{display:inline-block;width:30px;height:1px;background:var(--red)}
.about-title{left:161px;top:686px;font-size:27px;font-weight:600;color:var(--ink);text-transform:uppercase}
.about-bar{left:386px;top:609px;width:3px;height:168px;background:linear-gradient(var(--red) 0 33%,var(--ink) 33% 66%,var(--teal) 66%)}
.about-copy{left:463px;top:601px;width:575px;font-size:10px;line-height:19px;color:#666}
.about-copy p{margin-bottom:10px}

/* services */
.services{left:0;top:832px;width:1200px;height:479px;background:var(--cream)}
.sec-label{left:0;width:1200px;text-align:center;font-size:12px;color:var(--red);text-transform:uppercase;display:flex;justify-content:center;align-items:center;gap:8px}
.sec-title{left:0;width:1200px;text-align:center;font-size:27px;font-weight:600;color:var(--ink)}
.sec-desc{left:300px;width:600px;top:948px;text-align:center;font-size:13px;line-height:24px;color:var(--muted)}
.service-card{top:1035px;width:278px;height:223px;background:var(--white);border-radius:22px;box-shadow:0 3px 14px rgba(0,0,0,.08);padding:24px 30px;color:var(--ink)}
.service-card.featured{background:var(--red);color:var(--white)}
.service-card svg{display:block;width:52px;height:44px}
.service-name{font-family:"Dosis",sans-serif;font-weight:700;font-size:15.5px;margin-top:23px}
.service-text{font-size:10.5px;line-height:20px;margin-top:6px;color:var(--muted)}
.featured .service-text{color:var(--white)}
.service-more{font-size:10.5px;font-weight:700;margin-top:10px}

/* plans */
.plan-toggle{left:535px;top:1451px;width:136px;height:24px;background:var(--cream);border-radius:12px;font-size:9.5px;font-weight:700;display:flex;align-items:center}
.plan-toggle .on{background:var(--red);color:var(--white);border-radius:12px;height:24px;width:76px;display:flex;align-items:center;justify-content:center}
.plan-toggle .off{flex:1;text-align:center;color:var(--ink)}
.plan{top:1505px;width:278px;height:406px}
.plan-head{height:44px;background:var(--dark);color:var(--white);font-family:"Dosis",sans-serif;font-weight:700;font-size:17px;display:flex;align-items:center;justify-content:center}
.plan-price{height:75px;background:var(--teal);color:var(--white);text-align:center;padding-top:9px}
.plan-price b{font-family:"Dosis",sans-serif;font-size:29px;font-weight:700}
.plan-price small{font-size:12px}
.plan-price div{font-size:12.5px;margin-top:1px}
.plan-row{height:46px;display:flex;align-items:center;justify-content:center;font-size:11px;color:var(--muted);background:var(--row-b)}
.plan-row:nth-child(odd){background:var(--row-a)}
.plan-foot{height:57px;background:var(--row-a);display:flex;align-items:center;justify-content:center;margin-top:3px}
.plan-foot span{background:var(--red);color:var(--white);font-size:10.5px;padding:8px 14px;border-radius:2px}
.client{top:1962px;width:128px;height:66px;background:var(--cream);border:1px solid #efefe2;display:flex;align-items:center;justify-content:center;font-size:11.5px;color:#666;text-transform:uppercase}
.dots{left:583px;top:2058px;display:flex;gap:7px}
.dots i{width:5px;height:5px;border-radius:50%;background:#dde}
.dots i:first-child{background:var(--teal)}

/* contact */
.contact{left:0;top:2116px;width:1200px;height:330px;background:var(--red);color:var(--white)}
.contact-fade{left:0;top:2440px;width:1200px;height:50px;background:linear-gradient(var(--red),var(--white))}
.contact-label{left:161px;top:2164px;font-size:12px;color:var(--white);display:flex;align-items:center;gap:8px}
.contact-label .rule{background:var(--white)}
.contact-title{left:161px;top:2184px;font-size:26px;font-weight:600;color:var(--white)}
.contact-line{left:161px;font-size:15px;font-weight:700;color:var(--white);display:flex;align-items:center;gap:10px}
.contact-line em{font-style:normal;font-weight:500;font-size:14px}
.socials{left:161px;top:2329px;display:flex;gap:10px}
.socials span{width:31px;height:31px;border-radius:50%;border:1.5px solid var(--white);color:var(--white);font-size:9px;font-weight:700;display:flex;align-items:center;justify-content:center}
.socials span:first-child{background:var(--white);color:var(--red)}
.field{background:var(--white);color:#999;font-size:10.5px;padding:8px}
.send{left:461px;top:2315px;width:82px;height:30px;background:var(--dark);color:var(--white);font-size:10.5px;display:flex;align-items:center;justify-content:center}

/* footer */
.footer-brand{left:161px;top:2522px}
.footer-about{left:161px;top:2578px;width:425px;font-size:10px;line-height:19px;color:#444}
.footer-head{font-family:"Dosis",sans-serif;font-weight:700;font-size:13px;color:var(--ink);text-transform:uppercase;letter-spacing:.6px}
.footer-menu{left:686px;top:2520px}
.footer-menu ul{list-style:none;margin-top:16px;font-size:11px;line-height:19px;color:#444}
.footer-menu li:first-child{color:var(--red)}
.newsletter{left:838px;top:2520px;width:201px}
.newsletter .field{margin-top:14px;height:25px;border:1px solid #ddd;padding:6px 6px;font-size:9.5px;color:#777}
.newsletter .sub{margin-top:8px;height:29px;background:var(--teal);color:var(--white);font-size:10px;display:flex;align-items:center;justify-content:center;text-transform:uppercase}
.bottom-bar{left:0;top:2707px;width:1200px;height:37px;background:var(--dark);color:#bbb;font-size:10.5px;display:flex;align-items:center;justify-content:center}
.bottom-bar b{color:var(--teal);font-weight:400;margin:0 3px}
</style>
</head>
<body>

<header class="site-header abs">
  <div class="brand abs"><div class="brand-name">plumvista.net</div><div class="brand-tag">Simplifying the way you work</div></div>
  <nav class="main-nav abs"><span class="active">Home</span><span>About</span><span>Our Services</span><span>Features</span><span>Our Clients</span><span>Contact</span></nav>
  <div class="btn-signup abs"><svg width="8" height="9" viewBox="0 0 8 9"><rect x="0" y="4" width="8" height="5" fill="#fff"/><path d="M2 4V2.5a2 2 0 0 1 4 0V4" stroke="#fff" fill="none"/></svg>SIGN UP</div>
  <div class="btn-login abs"><svg width="8" height="9" viewBox="0 0 8 9"><circle cx="4" cy="2.5" r="2.2" fill="#fff"/><path d="M0 9a4 3.5 0 0 1 8 0z" fill="#fff"/></svg>LOGIN</div>
</header>

<section class="hero abs"></section>
<div class="hero-fade abs" role="img" aria-label="Soft cloud border between the hero and the about section"></div>
<h1 class="hero-title heading abs">Provide system security &amp; cloud based applications services</h1>
<p class="hero-sub abs">Lorem ipsum dolor sit amet, consectetur adipiscing elit, sed do eiusmod tempor incididunt ut labore et dolore magna aliqua.</p>
<div class="hero-btn abs">LEARN MORE <svg width="5" height="7" viewBox="0 0 5 7"><path d="M0 0l5 3.5L0 7z" fill="#f20f0c"/></svg></div>
<div class="hero-art abs" role="img" aria-label="Illustration of a red computer monitor with a padlock, shield, cloud, documents and folders"></div>

<div class="about-label abs"><span class="rule"></span>About Plumvista</div>
<h2 class="about-title heading abs">Who We Are</h2>
<div class="about-bar abs"></div>
<div class="about-copy abs">
  <p>Plumvista.net is an Australian based Software Company that provides individual technology solutions and professional software for clients worldwide. Our work is based on quality sales, customer and technical support services.</p>
  <p>Being oriented towards innovative productivity in our work, we come up with essential tools for online business enhancing. Our programming specialists focus on delivering solutions for small start-ups as well as large organizations and companies. The team of purposeful and experienced professionals works hard to extract maximum performance from modern information technologies.</p>
  <p>Providing the best quality of service and excellence of support we established a global presence in the software market. Our clients come from all over the world.</p>
</div>

<section class="services abs"></section>
<div class="sec-label abs" style="top:878px"><span class="rule"></span>Featured Services</div>
<h2 class="sec-title heading abs" style="top:898px">Solutions for System Security &amp; Cloud based Applications</h2>
<p class="sec-desc abs">Ut enim ad minim veniam, quis nostrud exercitation ullamco laboris nisi ut aliquip ex ea commodo consequat. Duis aute irure dolor in reprehenderit in voluptate nulla pariatur.</p>

<article class="service-card featured abs" style="left:161px">
  <svg viewBox="0 0 52 44" fill="none" stroke="#fff" stroke-width="2"><rect x="2" y="6" width="34" height="24" rx="2"/><path d="M12 38h16M20 30v8"/><path d="M38 4l10 4v8c0 7-5 11-10 13-5-2-10-6-10-13V8z" fill="#f20f0c"/></svg>
  <div class="service-name">System Support &amp; Security</div>
  <p class="service-text">Nemo enim ipsam voluptatem quia voluptas sit aspernatur aut odit aut fugit, sed quia consequuntur magni dolores</p>
  <div class="service-more">Read More</div>
</article>
<article class="service-card abs" style="left:461px">
  <svg viewBox="0 0 52 44" fill="none" stroke="#f20f0c" stroke-width="2"><path d="M12 34a9 9 0 0 1 0-18 12 12 0 0 1 23-3 9 9 0 0 1 4 21"/><rect x="18" y="18" width="15" height="22" rx="1" fill="#fff"/><path d="M21 24h9M21 29h9M21 34h6"/></svg>
  <div class="service-name">Cloud Based Applications</div>
  <p class="service-text">Nemo enim ipsam voluptatem quia voluptas sit aspernatur aut odit aut fugit, sed quia consequuntur magni dolores</p>
  <div class="service-more">Read More</div>
</article>
<article class="service-card abs" style="left:761px">
  <svg viewBox="0 0 52 44" fill="none" stroke="#f20f0c" stroke-width="2"><path d="M12 26a9 9 0 0 1 0-18 12 12 0 0 1 23-3 9 9 0 0 1 4 21z"/><path d="M25 26v8M14 34h22M14 34v4M25 34v4M36 34v4"/><circle cx="14" cy="40" r="2"/><circle cx="25" cy="40" r="2"/><circle cx="36" cy="40" r="2"/></svg>
  <div class="service-name">Hosting Solutions</div>
  <p class="service-text">Nemo enim ipsam voluptatem quia voluptas sit aspernatur aut odit aut fugit, sed quia consequuntur magni dolores</p>
  <div class="service-more">Read More</div>
</article>

<div class="sec-label abs" style="top:1362px"><span class="rule"></span>Choose Your Plan</div>
<h2 class="sec-title heading abs" style="top:1380px;text-transform:uppercase">Choose a plan that's right for you</h2>
<div class="plan-toggle abs"><span class="on">MONTHLY</span><span class="off">YEARLY</span></div>

<div class="plan abs" style="left:161px">
  <div class="plan-head">Starter</div>
  <div class="plan-price"><b>0</b><small> / mo</small><div>Our starter plan</div></div>
  <div><div class="plan-row">Nemo enim ipsam voluptatem</div><div class="plan-row">Nemo enim ipsam voluptatem</div><div class="plan-row">Nemo enim ipsam voluptatem</div><div class="plan-row">Nemo enim ipsam voluptatem</div><div class="plan-row">Nemo enim ipsam voluptatem</div></div>
  <div class="plan-foot"><span>Sign Up</span></div>
</div>
<div class="plan abs" style="left:461px">
  <div class="plan-head">Standard</div>
  <div class="plan-price"><b>0?</b><small> / mo</small><div>Our starter plan</div></div>
  <div><div class="plan-row">Nemo enim ipsam voluptatem</div><div class="plan-row">Nemo enim ipsam voluptatem</div><div class="plan-row">Nemo enim ipsam voluptatem</div><div class="plan-row">Nemo enim ipsam voluptatem</div><div class="plan-row">Nemo enim ipsam voluptatem</div></div>
  <div class="plan-foot"><span>Sign Up</span></div>
</div>
<div class="plan abs" style="left:761px">
  <div class="plan-head">Pro</div>
  <div class="plan-price"><b>0?</b><small> / mo</small><div>Our starter plan</div></div>
  <div><div class="plan-row">Nemo enim ipsam voluptatem</div><div class="plan-row">Nemo enim ipsam voluptatem</div><div class="plan-row">Nemo enim ipsam voluptatem</div><div class="plan-row">Nemo enim ipsam voluptatem</div><div class="plan-row">Nemo enim ipsam voluptatem</div></div>
  <div class="plan-foot"><span>Sign Up</span></div>
</div>

<div class="client abs" style="left:161px">Client Logo 1</div>
<div class="client abs" style="left:311px">Client Logo 2</div>
<div class="client abs" style="left:461px">Client Logo 3</div>
<div class="client abs" style="left:611px">Client Logo 4</div>
<div class="client abs" style="left:761px">Client Logo 5</div>
<div class="client abs" style="left:911px">Client Logo 6</div>
<div class="dots abs"><i></i><i></i><i></i></div>

<section class="contact abs"></section>
<div class="contact-fade abs" role="img" aria-label="Soft cloud border between the contact section and the footer"></div>
<div class="contact-label abs"><span class="rule"></span>QUICK CONTACT</div>
<h2 class="contact-title heading abs">GET IN TOUCH</h2>
<div class="contact-line abs" style="top:2245px"><svg width="13" height="13" viewBox="0 0 13 13"><path d="M3 0l2.5 3-1.5 2a8 8 0 0 0 4 4l2-1.5 3 2.5-1.5 2.5C6 13 0 7 .5 1.5z" fill="#fff"/></svg><em>Office:</em> +61 7 5550 1234</div>
<div class="contact-line abs" style="top:2279px"><svg width="10" height="15" viewBox="0 0 10 15"><rect x="1" y="1" width="8" height="13" rx="1.5" stroke="#fff" stroke-width="1.5" fill="none"/><circle cx="5" cy="11.5" r="1" fill="#fff"/></svg><em>Mobile:</em> +61 0400 555 018</div>
<div class="socials abs" aria-label="Social profiles"><span>Vox</span><span>Kel</span><span>Pim</span><span>Zed</span><span>Tuv</span></div>
<div class="field abs" style="left:461px;top:2166px;width:185px;height:31px">Your Name</div>
<div class="field abs" style="left:658px;top:2166px;width:185px;height:31px">Email</div>
<div class="field abs" style="left:854px;top:2166px;width:185px;height:31px">Phone</div>
<div class="field abs" style="left:461px;top:2208px;width:578px;height:91px">Message</div>
<div class="send abs">SEND</div>

<div class="footer-brand abs"><div class="brand-name">plumvista.net</div><div class="brand-tag">Simplifying the way you work</div></div>
<p class="footer-about abs">We have provided back end services, for example, system support and security and cloud based applications development solutions for a wide variety of industries. We are known for the quality of our work, affordable rates and our individual approach to each customer. Our company offers a wide variety of professional web solution and all this at very competitive prices!</p>
<div class="footer-menu abs"><div class="footer-head">Menu</div><ul><li>Home</li><li>About</li><li>Our Services</li><li>Features</li><li>Our Clients</li><li>Contact</li></ul></div>
<div class="newsletter abs"><div class="footer-head">Subscribe to our newsletter</div><div class="field">Enter Email</div><div class="sub">Subscribe</div></div>

<footer class="bottom-bar abs">© 2019 <b>plumvista.net</b> | All rights reserved.</footer>

</body>
</html>
```